****FLYER design - LAW FIRM ADVERTISEMENT****

We are a small law firm based in Los Angeles, CA. We need an flyer used for advertising that we will be passing out. We want the flyer to be about 4in x 6in.

We want the flyer to advertise the name of our firm: MARVELLO QUINTARD LLP (no period)
- We want our group photo to take up a good portion of the flyer (although it's okay if parts of the photo have wording over it.)

COLORS: Our firm colors are different shades of steal/metal grey with a bit of a bold orange accent. Any bold writing, like our slogan, names of practice areas,... should be in orange.

We envision a horizontal lay-out of the flyer, but are open to creative options laid out vertically!

Feel free to play with the fonts, the sizing, the color combinations,...

We want the flyer to advertise our two areas of practice: PERSONAL INJURY and EMPLOYMENT LAW. Please also place each photo icon of our areas of practice somewhere around the name (ambulance photo for personal injury; person behind computer desk for employment law). The icons can be relatively small.

Under Personal Injury, please write:
If you or a loved one are suffering from an injury or wrongful death caused by the careless or intentional acts of others, then you have the right to pursue compensation for your injury, out-of-pocket expenses, lost wages, emotional anguish, and more.

Under Employment Law, please write:
Our attorneys regularly represent clients in disputes involving sex, age and race discrimination, sexual harassment, retaliatory discharge, defamation, unlawful termination, breach of employment contracts, and more.

Somewhere on the flyer, please write our slogan IN ITALICS (and probably in orange):
- You Speak. We Listen. They Pay.

In somewhat bright and bold writing, please write "CONTACT US FOR A FREE CONSULTATION TODAY!" (maybe just after our slogan?)
- And under that phrase, write:
- 752 W. Folbrook Lane, Suite 400 Beverly Hills, CA 90210
phone: 310.555.8143
fax: 310.555.9261
email: info@mqmlegal.example
web: www.mqmlegal.example

If possible, and only if there's room without it looking too busy, somewhere in the upper left corner, place our "MQM" logo.
Updates

PLEASE NOTE THAT WE CHANGED OUR GROUP PHOTO TO A SLIGHTLY EDITED ONE.  PLEASE BE SURE TO USE THE NEW ONE!!!  (We deleted the old.)

Target Market(s)

employees, lower and mid-income individuals, minority communities. However, we still want the flyer to look sleek, modern, and professional.

Industry/Entity Type

Advertising

Requirements
Must have
• Firm Name,
Photo of Partners,
Names, photos, and small description of practice areas,
Firm slogan,
"Contact us for a free consultation today!",
Firm contact info.

And only if space and overall look permits, firm "MQM" logo.

We want an overall very sleek, modern feel to our flyer. While we do want to look professional, we wanted a more approachable feel than the typical, conservative law offices.
Nice to have
• Firm "MQM" logo

Horizontal lay out, though we're open to vertical options.

```html
<!DOCTYPE html>
<html lang="en">
<head>
<meta charset="utf-8">
<title>MARVELLO QUINTARD LLP — Flyer</title>
<link href="https://fonts.googleapis.com/css2?family=Yanone+Kaffeesatz:wght@300;400;700&display=swap" rel="stylesheet">
<style>
  :root {
    --page-bg: #ffffff;
    --flyer-light: #f3f3f3;
    --flyer-dark: #c3c3c3;
    --steel: #5b8593;
    --steel-text: #4d7886;
    --icon-tile: #1d3d40;
    --orange: #f26a2e;
    --white: #ffffff;
    --photo-dark: #3a2f24;
    --photo-mid: #6b5a40;
    --photo-light: #a89a7a;
  }
  * { margin: 0; padding: 0; box-sizing: border-box; }
  html, body {
    width: 912px; height: 1200px; overflow: hidden;
    background: var(--page-bg);
    font-family: "Yanone Kaffeesatz", "Arial Narrow", sans-serif;
  }
  .flyer {
    position: absolute; left: 56px; top: 0;
    width: 800px; height: 1200px; overflow: hidden;
    background: radial-gradient(ellipse 70% 55% at 50% 45%, var(--flyer-light) 0%, #dedede 55%, var(--flyer-dark) 100%);
  }
  .hero { position: absolute; left: 0; top: 0; width: 800px; height: 500px; }
  .logo {
    position: absolute; left: 28px; top: 23px; width: 196px; height: 196px;
    background: var(--steel);
    display: flex; align-items: center; justify-content: center;
  }
  .logo-name {
    color: var(--white); font-weight: 400; font-size: 84px; letter-spacing: 6px; line-height: 1;
  }
  .slogan {
    position: absolute; left: 33px; top: 380px;
    color: var(--orange); font-weight: 700; font-size: 68px; line-height: 82px;
    letter-spacing: -0.5px;
  }
  .practice { position: absolute; left: 39px; width: 740px; }
  .practice-injury { top: 564px; }
  .practice-employment { top: 782px; }
  .practice-head { display: flex; align-items: flex-end; gap: 8px; }
  .practice-icon { width: 83px; height: 83px; background: var(--icon-tile); flex: none; }
  .practice-title {
    color: var(--orange); font-weight: 400; font-size: 45px; line-height: 1; margin-bottom: -6px;
  }
  .practice-text {
    margin-top: 8px; color: var(--steel-text); font-weight: 300;
    font-size: 27px; line-height: 33px;
  }
  .contact {
    position: absolute; left: 0; top: 1010px; width: 800px; text-align: center;
  }
  .contact-call {
    color: var(--white); font-weight: 700; font-size: 55px; line-height: 1;
    margin-left: 48px;
  }
  .contact-address {
    margin-top: 14px; color: var(--orange); font-weight: 300; font-size: 25px; margin-left: 20px;
  }
  .contact-line {
    color: var(--orange); font-weight: 300; font-size: 25px; margin-left: 20px;
  }
  .contact-line.phone { margin-top: 10px; }
  .contact-line strong { color: var(--white); font-weight: 400; }
  .contact-line .big { font-size: 42px; }
  .contact-line .sep { margin: 0 10px; font-style: italic; }
</style>
</head>
<body>
  <main class="flyer">
    <svg class="hero" viewBox="0 0 800 500" xmlns="http://www.w3.org/2000/svg">
      <defs>
        <linearGradient id="photoTone" x1="0" y1="0" x2="1" y2="1">
          <stop offset="0" stop-color="var(--photo-mid)"/>
          <stop offset="0.45" stop-color="var(--photo-dark)"/>
          <stop offset="1" stop-color="var(--photo-light)"/>
        </linearGradient>
      </defs>
      <path role="img" aria-label="Group photo of the firm's three partners standing together"
            d="M107 0 H800 V480 C560 470 300 420 157 220 L107 220 Z"
            fill="url(#photoTone)"/>
      <path d="M157 220 C300 420 560 470 800 480" fill="none" stroke="var(--steel)" stroke-width="7"/>
    </svg>

    <div class="logo"><span class="logo-name">MQM</span></div>

    <h1 class="slogan">You Speak.<br>We Listen. They Pay.</h1>

    <section class="practice practice-injury">
      <div class="practice-head">
        <div class="practice-icon" role="img" aria-label="Ambulance icon"></div>
        <h2 class="practice-title">PERSONAL INJURY:</h2>
      </div>
      <p class="practice-text">If you or a loved one are suffering from an injury or wrongful death caused by the<br>careless or intentional acts of others, then you have the right to pursue compensation<br>for your injury, out-of-pocket expenses, lost wages, emotional anguish, and more. .</p>
    </section>

    <section class="practice practice-employment">
      <div class="practice-head">
        <div class="practice-icon" role="img" aria-label="Person at computer desk icon"></div>
        <h2 class="practice-title">EMPLOYMENT LAW:</h2>
      </div>
      <p class="practice-text">Our attorneys regularly represent clients in disputes involving sex, age and race<br>discrimination, sexual harassment, retaliatory discharge, defamation, unlawful<br>termination, breach of employment contracts, and more.</p>
    </section>

    <section class="contact">
      <p class="contact-call">Contact Us For A Free Consultation Today!</p>
      <p class="contact-address">752 W. Folbrook Lane, Suite 400 Beverly Hills, CA 90210</p>
      <p class="contact-line phone">phone: <strong class="big">310.555.8143</strong><span class="sep">//</span>fax: 310.555.9261</p>
      <p class="contact-line">email: <strong>info@mqmlegal.example</strong><span class="sep">//</span>web: <strong>www.mqmlegal.example</strong></p>
    </section>
  </main>
</body>
</html>
```